Wordpress Design Project

Specifications - we are after the design for a Wordpress Template. The template files need to be uploaded through the Wordpress templates upload button.
Lumigrid button required please
The template must also work and integrate with Wordpress.
We are after a sharp, professional look, that will be appealing to business clients as well as other customers requiring this service
refer to www.the-tulip-works.com.au
www.lanterns-korvi.com.au
Please create a logo.

Client Industry - Corporate and Mobile Massage
Header Colour - Charcoal/black with Purple/Crimson. All lettering on the header should appear in white or purple
Page colour - white
Other - rhs sidebar; easy to insert images on pages
Toolbar - horizontal below header - refer to two sites above for ideas.
This will be a 5 - 7 page site only.

Target Market(s)

Corporate and business massage - large businesses/government departments

Requirements
Must have
• The template files need to be uploaded through the Wordpress templates upload button.
Nice to have
• A logo

```html
<!DOCTYPE html>
<html lang="en">
<head>
<meta charset="utf-8">
<title>calm current – on location &amp; workplace massage</title>
<link rel="stylesheet" href="https://fonts.googleapis.com/css2?family=Source+Sans+3:wght@400;600&family=Tinos&display=swap">
<style>
:root{
  --purple:#8e1fc4;
  --purple-deep:#6a2a8a;
  --purple-btn:#6e2c8f;
  --purple-soft:#b06ad0;
  --header-dark:#1c1420;
  --header-mid:#3a2142;
  --nav-black:#1a1a1a;
  --panel-white:#ffffff;
  --bar-grey:#e6e6e6;
  --line-grey:#d6d6d6;
  --text:#555555;
  --text-dark:#222222;
  --sans:"Source Sans 3", Arial, sans-serif;
  --serif:"Tinos", "Times New Roman", serif;
}
*{box-sizing:border-box;margin:0;padding:0}
html,body{width:924px;height:1200px;overflow:hidden}
body{position:relative;font-family:var(--sans);color:var(--text);
  background:linear-gradient(180deg,#2a1a2e 0%,#241a27 85%,#3a1f46 100%)}
.abs{position:absolute}

/* header */
.site-header{left:0;top:0;width:924px;height:142px;
  background:radial-gradient(ellipse at 50% 0%,var(--header-mid) 0%,var(--header-dark) 75%);
  border-top:4px solid #5a2a72}
.brand-name{left:52px;top:34px;font-size:56px;font-weight:600;color:var(--purple);letter-spacing:-1px;line-height:1}
.brand-tagline{left:76px;top:88px;font-size:19px;color:#b85ae0;line-height:1}
.header-phone{left:788px;top:20px;font-size:14px;color:#fff;display:flex;align-items:center;gap:4px}
.social-list{left:762px;top:55px;display:flex;gap:7px}
.social-list span{width:20px;height:20px;background:#8a8a8a;border-radius:2px;display:block}
.search-box{left:704px;top:92px;width:202px;height:27px;background:#1a0f1e;border:1px solid #3b2a44;
  color:#ddd;font-size:12px;padding:5px 11px}
.search-box svg{position:absolute;right:6px;top:6px}

/* nav */
.main-nav{left:0;top:142px;width:924px;height:38px;background:var(--nav-black)}
.nav-item{top:0;height:38px;line-height:38px;font-size:15px;color:#eee}
.nav-item.is-active{background:var(--purple);color:#fff;text-align:center}
.nav-sep{top:10px;width:6px;height:18px;
  background-image:radial-gradient(#444 1px,transparent 1.2px);background-size:3px 3px}

/* hero */
.hero{left:0;top:180px;width:924px;height:432px}
.hero-photo{left:0;top:0;width:924px;height:432px;
  background:linear-gradient(90deg,#e9ecef 0%,#f3f4f6 40%,#eef0f0 65%,#9ab08a 88%,#5d7a52 100%)}
.hero-title{left:518px;top:125px;font-family:var(--serif);font-size:40px;line-height:45px;color:var(--text-dark)}
.hero-title span{display:block;padding-left:18px}
.hero-text{left:518px;top:222px;width:330px;font-size:11px;line-height:16.5px;color:#333;text-align:justify}
.hero-band{left:0;top:370px}

/* content panel */
.content-panel{left:10px;top:612px;width:904px;height:516px;background:var(--panel-white);
  border-left:2px solid #9060b0;border-right:2px solid #9060b0;border-bottom:2px solid #9060b0;
  border-radius:0 0 12px 12px}
.section-title{font-size:23px;color:var(--purple-deep);line-height:1}
.welcome-text{left:30px;top:668px;width:580px;font-size:11.5px;line-height:16.3px;text-align:justify}

.benefit-frame{left:32px;top:828px;width:286px;height:116px;border:2px solid #bbb;border-radius:6px;padding:5px;background:#f2f2f2}
.benefit-photo{width:100%;height:100%;border-radius:3px;
  background:linear-gradient(120deg,#e9b59a 0%,#d88c6e 45%,#e86a8a 80%,#f3c9d2 100%)}
.benefit-col{top:955px;width:130px}
.benefit-heading{font-size:14px;color:#222;display:flex;align-items:center;gap:3px;height:16px}
.benefit-heading i{display:block;width:14px;height:15px;background:#777;border-radius:2px}
.benefit-list{list-style:none;margin-top:12px}
.benefit-list li{font-size:11.5px;height:21.4px;display:flex;align-items:center;gap:3px}
.benefit-list li::before{content:"";width:11px;height:11px;border-radius:50% 0 50% 0;background:#c8c8c8}
.read-more{font-size:11.5px;color:var(--purple-deep);text-align:right;margin-top:3px;padding-right:2px}

.testimonial{left:348px;width:268px;height:76px}
.testimonial svg{position:absolute;left:0;top:0}
.testimonial p{position:absolute;left:27px;top:4px;width:220px;font-size:11px;line-height:17px;color:#444}
.testimonial cite{position:absolute;right:28px;top:58px;font-style:normal;font-size:11px;color:#888}

.column-divider{left:628px;top:630px;width:1px;height:470px;background:var(--line-grey)}

/* sidebar */
.side-bar-title{left:647px;width:259px;height:27px;background:var(--bar-grey);
  font-size:19px;color:var(--purple-deep);padding:2px 10px;line-height:23px}
.field{left:647px;width:259px;height:27px;border:1px solid #ccc;border-radius:3px;
  font-size:11.5px;color:#555;padding:5px 13px}
.btn{background:var(--purple-btn);color:#fff;font-size:12px;text-align:center;border-radius:2px}
.blog-photo{left:649px;top:818px;width:257px;height:109px;
  background:linear-gradient(110deg,#f4f1ee 0%,#e3cbbb 45%,#c79b86 75%,#eee 100%)}
.blog-caption{left:649px;top:899px;width:257px;height:28px;background:rgba(20,20,20,.75);
  color:#fff;font-size:11px;padding:6px 21px}
.blog-text{left:654px;top:940px;width:248px;font-size:11px;line-height:16.5px;color:#333;text-align:justify}

/* footer */
.footer-links{left:0;top:1143px;width:924px;text-align:center;font-size:11.5px;color:var(--purple-soft)}
.footer-links b{font-weight:400;margin:0 6px;color:#8a5aa0}
.footer-copy{left:0;top:1168px;width:924px;text-align:center;font-size:11.5px;color:#9c4fc0}
</style>
</head>
<body>

<header class="site-header abs">
  <div class="brand-name abs">calm current</div>
  <div class="brand-tagline abs">on location &amp; workplace massage</div>
  <div class="header-phone abs">
    <svg width="9" height="16" viewBox="0 0 9 16"><path d="M2 1h3l-1 4-1.6.8c.4 2 1 3.6 2.3 5L6.5 10 9 12.5 7 15C3 13.5 0 7 2 1z" fill="#8e1fc4"/></svg>
    ( 555 ) 014-2380
  </div>
  <div class="social-list abs" aria-label="Social links"><span></span><span></span><span></span><span></span><span></span></div>
  <div class="search-box abs">Search
    <svg width="14" height="14" viewBox="0 0 14 14"><circle cx="5.5" cy="5.5" r="4.3" fill="none" stroke="#ccc" stroke-width="1.5"/><path d="M8.7 8.7 13 13" stroke="#ccc" stroke-width="1.6"/></svg>
  </div>
</header>

<nav class="main-nav abs">
  <div class="nav-item is-active abs" style="left:203px;width:73px">Home</div>
  <div class="nav-sep abs" style="left:289px"></div>
  <div class="nav-item abs" style="left:318px">About us</div>
  <div class="nav-sep abs" style="left:393px"></div>
  <div class="nav-item abs" style="left:428px">Packages</div>
  <div class="nav-sep abs" style="left:512px"></div>
  <div class="nav-item abs" style="left:551px">Profile</div>
  <div class="nav-sep abs" style="left:620px"></div>
  <div class="nav-item abs" style="left:652px">Contact</div>
</nav>

<section class="hero abs">
  <div class="hero-photo abs" role="img" aria-label="Photo of a woman meditating cross-legged outdoors with trees behind"></div>
  <h1 class="hero-title abs" style="font-weight:400">Restoring Balance<span>and Natural health</span></h1>
  <p class="hero-text abs">It was popularised in the 1960s with the release of Tessaline sheets containing Lorem Ipsum passages, and more recently with desktop publishing software like Quillset Layout including versions of Lorem Ipsum</p>
  <svg class="hero-band abs" width="924" height="62" viewBox="0 0 924 62">
    <polygon points="0,30 924,4 924,62 0,62" fill="#c9c9c9"/>
    <polygon points="0,44 924,16 924,62 0,62" fill="#d2d2d2"/>
    <rect x="0" y="44" width="924" height="18" fill="#222"/>
    <polygon points="0,44 924,16 924,42 0,44" fill="#cdcdcd"/>
    <g fill="#888"><circle cx="833" cy="50" r="4.5"/><circle cx="859" cy="50" r="4.5"/><circle cx="873" cy="50" r="4.5"/><circle cx="887" cy="50" r="4.5"/></g>
    <circle cx="846" cy="50" r="4.5" fill="#ddd"/>
  </svg>
</section>

<main class="content-panel abs"></main>

<h2 class="section-title abs" style="left:30px;top:630px;font-weight:400">Welcome</h2>
<p class="welcome-text abs">On the other hand, we denounce with righteous indignation and dislike men who are so beguiled and demoralized by the charms of pleasure of the moment, so blinded by desire, that they cannot foresee the pain and trouble that are bound to ensue; and equal blame belongs to those who fail in their duty through weakness of will, which is the same as saying through shrinking from toil and pain. These cases are perfectly simple and easy to distinguish.The standard chunk of Lorem Ipsum used since the 1500s is reproduced below for those interested. Sections 1.10.32 and 1.10.33 from "de Finibus Bonorum et Malorum" by Marcus Orvell are also reproduced in their exact original form, accompanied</p>

<h2 class="section-title abs" style="left:30px;top:793px;font-weight:400">Benefits</h2>
<div class="benefit-frame abs"><div class="benefit-photo" role="img" aria-label="Photo of hands massaging with a pink lotus flower"></div></div>

<div class="benefit-col abs" style="left:30px">
  <div class="benefit-heading"><i></i>Massage</div>
  <ul class="benefit-list"><li>Pellentesque interdum</li><li>Pellentesque interdum</li><li>Pellentesque interdum</li><li>Pellentesque interdum</li><li>Pellentesque interdum</li></ul>
  <div class="read-more">Read more</div>
</div>
<div class="benefit-col abs" style="left:186px">
  <div class="benefit-heading"><i></i>Yoga</div>
  <ul class="benefit-list"><li>Pellentesque interdum</li><li>Pellentesque interdum</li><li>Pellentesque interdum</li><li>Pellentesque interdum</li><li>Pellentesque interdum</li></ul>
  <div class="read-more">Read more</div>
</div>

<h2 class="section-title abs" style="left:352px;top:793px;font-weight:400">Client Testimonials</h2>

<div class="testimonial abs" style="top:830px">
  <svg width="268" height="76" viewBox="0 0 268 76" fill="none" stroke="#cfcfcf" stroke-width="4" stroke-linecap="round">
    <path d="M14 3c-6 0-8 3-8 8v18c0 5-2 8-5 9 3 1 5 4 5 9v18c0 5 2 8 8 8"/>
    <path d="M254 3c6 0 8 3 8 8v18c0 5 2 8 5 9-3 1-5 4-5 9v18c0 5-2 8-8 8"/>
  </svg>
  <p>It was popularised in the 1960s with the release of Tessaline sheets containing Lorem Ipsum passages.</p>
  <cite>Daniel Reyes</cite>
</div>
<div class="testimonial abs" style="top:915px">
  <svg width="268" height="76" viewBox="0 0 268 76" fill="none" stroke="#cfcfcf" stroke-width="4" stroke-linecap="round">
    <path d="M14 3c-6 0-8 3-8 8v18c0 5-2 8-5 9 3 1 5 4 5 9v18c0 5 2 8 8 8"/>
    <path d="M254 3c6 0 8 3 8 8v18c0 5 2 8 5 9-3 1-5 4-5 9v18c0 5-2 8-8 8"/>
  </svg>
  <p>It was popularised in the 1960s with the release of Tessaline sheets containing Lorem Ipsum passages.</p>
  <cite>Daniel Reyes</cite>
</div>
<div class="testimonial abs" style="top:1000px">
  <svg width="268" height="76" viewBox="0 0 268 76" fill="none" stroke="#cfcfcf" stroke-width="4" stroke-linecap="round">
    <path d="M14 3c-6 0-8 3-8 8v18c0 5-2 8-5 9 3 1 5 4 5 9v18c0 5 2 8 8 8"/>
    <path d="M254 3c6 0 8 3 8 8v18c0 5 2 8 5 9-3 1-5 4-5 9v18c0 5-2 8-8 8"/>
  </svg>
  <p>It was popularised in the 1960s with the release of Tessaline sheets containing Lorem Ipsum passages.</p>
  <cite>Daniel Reyes</cite>
</div>

<div class="column-divider abs"></div>
<svg class="abs" style="left:621px;top:871px" width="15" height="15" viewBox="0 0 15 15" fill="#d0d0d0"><circle cx="7.5" cy="7.5" r="3"/><circle cx="7.5" cy="2" r="2"/><circle cx="7.5" cy="13" r="2"/><circle cx="2" cy="7.5" r="2"/><circle cx="13" cy="7.5" r="2"/></svg>

<aside>
  <div class="side-bar-title abs" style="top:629px">Stay conncted</div>
  <div class="field abs" style="top:668px">First name</div>
  <div class="field abs" style="top:705px">Email Address</div>
  <div class="btn abs" style="left:842px;top:741px;width:64px;height:28px;line-height:28px">Submit</div>

  <div class="side-bar-title abs" style="top:780px">Latest Blog Posts</div>
  <svg class="abs" style="left:883px;top:788px" width="14" height="12" viewBox="0 0 14 12" fill="none" stroke="#888" stroke-width="2"><path d="M5 1 1 6l4 5M9 1l4 5-4 5"/></svg>
  <div class="blog-photo abs" role="img" aria-label="Photo of a client relaxing during a head massage"></div>
  <div class="blog-caption abs">Posted by name</div>
  <p class="blog-text abs">This book is a treatise on the theory of ethics, very popular during the Renaissance.Various versions have evolved over the years</p>
  <div class="btn abs" style="left:842px;top:993px;width:64px;height:28px;line-height:28px">Read more</div>

  <div class="side-bar-title abs" style="top:1029px">Newsletter Signup</div>
  <div class="field abs" style="top:1070px;width:229px">Email Address</div>
  <div class="btn abs" style="left:876px;top:1070px;width:30px;height:27px;line-height:27px">Go</div>
</aside>

<footer>
  <div class="footer-links abs">Home<b>|</b>About us<b>|</b>Packages<b>|</b>Profile<b>|</b>Contact</div>
  <div class="footer-copy abs">2012 © copyrights.calmcurrent.received</div>
</footer>

</body>
</html>
```